Mental Health

QRT HAVEN
Behavioral Health
4172 W. Pell St. Mesa, AZ 85219
Gwendolyn (480)555-0142 / Omar 480-555-0187

Email: QRTHaven@Mailvex.example
Newly Remodeled & Spacious
g Staff
Registered Nurses
Licensed Independent &
Professional Substance &
Abuse Counselors
Behavioral Health Techs
Certified Caregivers
Behavioral Health &
Substance Abuse Professionals

To Refer a Patient
About Us
QRT Haven is a Fully Staffed Behavioral
Health Residential Facility, providing
treatment plans for adults suffering
with various Behavioral Health and
Substance Abuse disorders, while living
in a nice safe, clean and supportive
environment. Our home offers clients the
ability to learn the necessary skills to
help clients adapt, build self confidence
as well as independence, with the goal
of reducing the probability of a future
crisis or possible relapse. We offer
counseling programs, consisting of a
variety of addiction and recovery support
groups, independent living, coping and
social skills groups, as well as assisting
clients with using tools to create a resume
to help obtain employment and so much
more. We are committed to teaching
self management care and allowing
clients to understand how to utilize the
resources, skills and tools available for
long term success by providing superior
quality, all-inclusive living arrangements
and treatment options.

Thank you for your patience while I update the final content needed for us to make the final decision this week.

```html
<!DOCTYPE html>
<html lang="en">
<head>
<meta charset="utf-8">
<title>QRT Haven Business Card</title>
<link href="https://fonts.googleapis.com/css2?family=Cinzel:wght@400&family=Roboto:wght@300;400&family=Montserrat:wght@500&display=swap" rel="stylesheet">
<style>
  :root {
    --stage: #232323;
    --card: #1e1e20;
    --card-edge: #2c2c2f;
    --brand-blue: #1a6fc0;
    --brand-green: #7db53c;
    --tagline: #9bb23a;
    --gold: #a8832c;
    --text: #e6e6e6;
    --text-soft: #cfcfcf;
    --web-green: #6e9c3c;
  }
  * { margin: 0; padding: 0; box-sizing: border-box; }
  html, body { width: 1200px; height: 1200px; overflow: hidden; background: var(--stage); }
  .stage { position: relative; width: 1200px; height: 1200px; }

  .card {
    position: absolute;
    width: 348px; height: 592px;
    background: var(--card);
    border: 1px solid var(--card-edge);
    border-radius: 22px;
    overflow: hidden;
    text-align: center;
    font-family: "Roboto", sans-serif;
    font-weight: 300;
    color: var(--text);
  }
  .card-front { left: 215px; top: 293px; }
  .card-back  { left: 652px; top: 298px; }

  .mark-dot {
    position: absolute; left: 50%;
    width: 96px; height: 96px; margin-left: -48px;
    border-radius: 50%;
    background: var(--brand-blue);
  }
  .card-front .mark-dot { top: 52px; }
  .card-back .mark-dot { top: 56px; }

  .backdrop-circle {
    position: absolute; left: 50%; top: 20px;
    width: 400px; height: 400px; margin-left: -200px;
    border-radius: 50%;
    background: rgba(255,255,255,0.025);
  }

  .brand-name {
    position: absolute; left: 0; right: 0;
    font-family: "Cinzel", serif;
    font-weight: 400;
    font-size: 40px;
    letter-spacing: 1px;
    color: var(--brand-blue);
    line-height: 1;
  }
  .card-front .brand-name { top: 173px; }
  .card-back .brand-name { top: 180px; }

  .brand-tagline {
    position: absolute; left: 0; right: 0; top: 224px;
    font-family: "Montserrat", sans-serif;
    font-weight: 500;
    font-size: 12.5px;
    letter-spacing: 6px;
    color: var(--tagline);
  }

  .person-name {
    position: absolute; left: 0; right: 0; top: 286px;
    font-family: "Cinzel", serif;
    font-size: 25px;
    letter-spacing: 1px;
    color: var(--brand-blue);
    line-height: 1;
  }
  .person-role {
    position: absolute; left: 0; right: 0; top: 313px;
    font-size: 15.5px;
    color: var(--text-soft);
  }

  .contact-divider {
    position: absolute; left: 52px; right: 52px; top: 351px;
    height: 26px;
  }

  .contact-lines {
    position: absolute; left: 0; right: 0; top: 391px;
    font-size: 15.5px; line-height: 25px;
    color: var(--text-soft);
  }
  .contact-address {
    position: absolute; left: 0; right: 0; top: 482px;
    font-size: 15.5px;
    color: var(--text-soft);
  }

  .footer-band {
    position: absolute; left: 0; right: 0; bottom: 0;
    height: 50px;
    background: linear-gradient(90deg, var(--brand-green), #2f8c8a 55%, var(--brand-blue));
    font-family: "Montserrat", sans-serif;
    font-weight: 500;
    font-size: 12.5px;
    letter-spacing: 6px;
    color: #ffffff;
    line-height: 50px;
    padding-left: 6px;
  }

  .service-list {
    position: absolute; left: 38px; right: 38px; top: 277px;
    list-style: none;
  }
  .service-list li {
    height: 30.3px; line-height: 29px;
    font-size: 15.5px; font-weight: 400;
    color: var(--text);
    border-bottom: 1px solid var(--gold);
    white-space: nowrap;
  }
  .service-list li:last-child { border-bottom: none; }

  .web-address {
    position: absolute; left: 0; right: 0; top: 549px;
    font-size: 16px;
    letter-spacing: 3px;
    color: var(--web-green);
  }
</style>
</head>
<body>
<main class="stage">

  <section class="card card-front">
    <div class="mark-dot"></div>
    <h1 class="brand-name">QRT HAVEN</h1>

    <p class="person-name">GWENDOLYN</p>
    <p class="person-role">Managing Director</p>

    <svg class="contact-divider" viewBox="0 0 244 26" aria-hidden="true">
      <line x1="0" y1="13" x2="68" y2="13" stroke="#7db53c" stroke-width="2"/>
      <line x1="176" y1="13" x2="244" y2="13" stroke="#2a86a8" stroke-width="2"/>
      <g fill="none" stroke="#5aa46a" stroke-width="1.4">
        <circle cx="94" cy="13" r="11.5"/>
        <circle cx="122" cy="13" r="11.5"/>
        <circle cx="150" cy="13" r="11.5"/>
      </g>
      <path d="M89 10 q5 -4 10 0 v2 h-2.5 v-1.5 h-5 v1.5 h-2.5z M90.5 13 h7 v4.5 h-7z" fill="#4e9d8a"/>
      <rect x="116" y="9" width="12" height="8.5" fill="none" stroke="#6aa84a" stroke-width="1.3"/>
      <path d="M116 9 l6 5 l6 -5" fill="none" stroke="#6aa84a" stroke-width="1.3"/>
      <g fill="none" stroke="#3f8fb0" stroke-width="1.1">
        <circle cx="150" cy="13" r="6"/>
        <ellipse cx="150" cy="13" rx="2.6" ry="6"/>
        <line x1="144" y1="13" x2="156" y2="13"/>
      </g>
    </svg>

    <div class="contact-lines">
      <p>(480) 555-0142</p>
      <p>QRTHaven@Mailvex.example</p>
      <p>www.qrthavenaz.example</p>
    </div>
    <p class="contact-address">4172 W. Pell St. Mesa, AZ 85219</p>

    <div class="footer-band">BEHAVIORAL HEALTH</div>
  </section>

  <section class="card card-back">
    <div class="backdrop-circle"></div>
    <div class="mark-dot"></div>
    <h2 class="brand-name">QRT HAVEN</h2>
    <p class="brand-tagline">BEHAVIORAL HEALTH</p>

    <ul class="service-list">
      <li>Newly Remodeled &nbsp;|&nbsp; Spacious Staff</li>
      <li>Registered Nurses | &nbsp;Abuse Counselors</li>
      <li>Licensed Independent</li>
      <li>Professional Substance</li>
      <li>Behavioral Health Techs</li>
      <li>Certified Caregivers</li>
      <li>Behavioral Health</li>
      <li>Substance Abuse Professionals</li>
    </ul>

    <p class="web-address">www.qrthavenaz.example</p>
  </section>

</main>
</body>
</html>
```